Concert Poster

Dear all!
It seems that we have found our final design!
Thanks a lot for your contribution so far. It is not necessary to post any more designs.

BR Jonas

____________________
For the band Velvet Groove - we would like to have a standard concert announcement poster that we can use to advertise for our gigs.The band plays the classic songs of the disco era end of the 70ies, e.g. Lusk, Vera Castell, Stone Rain & Ash, Brisk & The Crew etc. On stage we also adapt to the fashion of those times, but in a modern manner.See more details on our website: www.velvetgroove-band.de

We intend to position the band in the high price segment - so that poster should be positively effective even between posters of famous bands.

Format: DIN-A1 Portrait - 594 x 841 mm

If possible, it would also be great if we could use the same design to print flyers (format DIN-A6).

Target Market(s)

Live Music Bands

Requirements
Must have
• The poster should contain:
• - Our logo (see uploads)
• - Our official photo (see uploads)
• - Text about date, venue, time, entrance fee or the concert AND
• alternatively a possibility to leave this space blank so that we can print a bunch of empty posters that we can write the details on manually (to avoid printing posters for each gig individually)
• - Information about the Band:
• - Website: www.velvetgroove-band.de
• - Like us on facebook: fb/velvetgroovebavaria

```html
<!DOCTYPE html>
<html lang="en">
<head>
<meta charset="utf-8">
<title>Velvet Groove – Disco Night Concert Poster</title>
<link href="https://fonts.googleapis.com/css2?family=League+Gothic&family=Roboto:wght@500;700&display=swap" rel="stylesheet">
<style>
  :root {
    --page: #e9e9e9;
    --navy: #0f1b30;
    --navy-light: #1d3455;
    --orange: #f26a12;
    --amber: #f7a515;
    --yellow: #fbb91c;
    --red: #d0121c;
    --ink: #0a0a0a;
    --white: #ffffff;
    --gold: #f6b21b;
  }
  * { box-sizing: border-box; margin: 0; padding: 0; }
  html, body { width: 1200px; height: 1200px; overflow: hidden; background: var(--page); }
  .poster {
    position: absolute; left: 205px; top: 40px; width: 791px; height: 1120px;
    background: radial-gradient(ellipse at 60% 45%, var(--navy-light) 0%, var(--navy) 70%, #081020 100%);
    overflow: hidden;
  }
  .photo { position: absolute; left: 33px; width: 342px; border: 4px solid var(--white); }
  .photo--singer { top: 43px; height: 319px; background: linear-gradient(135deg, #c98a5a, #f1c8a4 50%, #8a5a2c); }
  .photo--band { top: 388px; height: 347px; background: linear-gradient(180deg, #c0c0c4 0%, #a43548 35%, #3a2a2a 75%, #d8d8d8 100%); }
  .photo--guitarist { top: 761px; height: 312px; background: linear-gradient(135deg, #d06a5e, #c98a6a 50%, #4a2b22); }

  .brand { position: absolute; left: 419px; width: 330px; top: 40px; text-align: center; }
  .brand__dot { width: 92px; height: 92px; border-radius: 50%; background: var(--gold); margin: 0 auto 12px; }
  .brand__name {
    font-family: "League Gothic", sans-serif; font-weight: 400; color: var(--gold);
    font-size: 64px; line-height: 0.95; letter-spacing: 3px; text-transform: uppercase;
  }

  .info {
    position: absolute; left: 419px; width: 330px; top: 293px; bottom: 0;
    background: linear-gradient(180deg, var(--orange) 0%, var(--amber) 8%, var(--yellow) 30%, var(--yellow) 100%);
    font-family: "League Gothic", sans-serif; color: var(--ink); text-align: center;
    overflow: hidden;
  }
  .info p, .info span { white-space: nowrap; }
  .band-red {
    position: absolute; left: 0; right: 0; background: var(--red); color: var(--white);
    font-family: "League Gothic", sans-serif; text-transform: uppercase; white-space: nowrap;
    display: flex; align-items: center; justify-content: center;
  }
  .date { top: 43px; height: 47px; font-size: 38px; }
  .presents { position: absolute; top: 98px; left: 0; right: 0; }
  .presents__title { font-size: 46px; line-height: 1; text-transform: uppercase; }
  .presents__claim { font-family: "Roboto", sans-serif; font-weight: 700; font-size: 30px; line-height: 1.1; margin-top: 4px; }
  .presents__text { font-family: "Roboto", sans-serif; font-weight: 500; font-size: 18px; line-height: 1.4; margin-top: 8px; white-space: normal !important; }
  .divider { position: absolute; top: 263px; left: 0; right: 0; height: 2px; background: #b57c0e; }
  .headline { position: absolute; top: 278px; left: 0; right: 0; font-weight: 400; text-transform: uppercase; }
  .headline__line { display: block; line-height: 0.8; transform: scaleY(1.4); transform-origin: top center; }
  .headline__top { font-size: 80px; }
  .headline__main { position: absolute; left: 0; right: 0; top: 92px; font-size: 114px; }
  .venue { top: 531px; height: 47px; font-size: 38px; }
  .facts {
    position: absolute; top: 594px; left: 0; right: 0; height: 95px; background: var(--navy);
    display: flex; justify-content: space-between; padding: 9px 14px;
  }
  .fact { width: 139px; background: var(--white); display: flex; flex-direction: column; align-items: center; justify-content: center; }
  .fact__value { font-family: "League Gothic", sans-serif; font-size: 48px; line-height: 0.9; }
  .fact__label { font-family: "Roboto", sans-serif; font-weight: 700; font-size: 19px; line-height: 1.1; }
  .contact {
    position: absolute; top: 689px; left: 0; right: 0; bottom: 0;
    background: linear-gradient(180deg, var(--yellow), var(--amber) 60%, var(--orange));
    padding-top: 26px;
  }
  .contact__web { font-size: 28px; line-height: 1.1; }
  .contact__social { font-size: 22px; line-height: 1.1; margin-top: 12px; }
</style>
</head>
<body>
  <main class="poster">
    <div class="photo photo--singer" role="img" aria-label="Portrait of the smiling lead singer with blonde hair and gold earrings"></div>
    <div class="photo photo--band" role="img" aria-label="Official band photo: seven musicians in disco outfits holding a mirror ball"></div>
    <div class="photo photo--guitarist" role="img" aria-label="Portrait of a band member wearing round red sunglasses"></div>

    <header class="brand">
      <div class="brand__dot"></div>
      <h1 class="brand__name">Velvet<br>Groove</h1>
    </header>

    <section class="info">
      <div class="band-red date">Friday, 23 November 2018</div>
      <div class="presents">
        <p class="presents__title">Velvet Groove Presnts</p>
        <p class="presents__claim">Hot. Funky. Live.</p>
        <p class="presents__text">The Munich disco &amp; funk party<br>band with dance guarantee</p>
      </div>
      <div class="divider"></div>
      <h2 class="headline">
        <span class="headline__line headline__top">Disco Night</span>
        <span class="headline__line headline__main">Concert</span>
      </h2>
      <div class="band-red venue">Music Club Munich</div>
      <div class="facts">
        <div class="fact"><span class="fact__value">9,00 €</span><span class="fact__label">entry ticket</span></div>
        <div class="fact"><span class="fact__value">20.00</span><span class="fact__label">entry time</span></div>
      </div>
      <footer class="contact">
        <p class="contact__web">For more info: www.velvetgroove-band.de</p>
        <p class="contact__social">Like us on facebook: fb/velvetgroovebavaria</p>
      </footer>
    </section>
  </main>
</body>
</html>
```